Verdant Pathworks Business Card

want the back of card to be blue- with the logo in the center
front of card- info plus logo (info being mailing address, email address, and website address )
4 different names with titles to have on cards
1) Dominic Ashvale - Owner
2) Bethany Korvuth- Customer Relationship Specialist
3) Luca Brennwick- Vice President of Sales
4) Neil Umbright- Chief Technology Officer

Target Market(s)

tech company in the government/probation office industry

Industry/Entity Type

Government Office

Contact Information for Business Card

1) Dominic Ashvale - Owner

Colors
0355a3
ffffff

Requirements
Must have
• back side should be blue, with the logo placed in the center
• front side needs to include both the logo, as well as company info (info should include website address, email address, and mailing address)

```html
<!DOCTYPE html>
<html lang="en">
<head>
<meta charset="utf-8">
<title>Verdant Pathworks Business Cards</title>
<link rel="stylesheet" href="https://fonts.googleapis.com/css2?family=Open+Sans:wght@400;600;700&display=swap">
<style>
  :root {
    --navy: #223d70;
    --white: #ffffff;
    --grey-band: #c4c7cd;
    --grey-soft: #e6e7ea;
    --stage: #2a2a2a;
    --text-soft: #d5dcea;
  }
  * { margin: 0; padding: 0; box-sizing: border-box; }
  html, body { width: 1200px; height: 2684px; overflow: hidden; background: var(--stage); }
  body { font-family: "Open Sans", sans-serif; }
  .card-set { position: relative; width: 1200px; height: 894px; }
  .card {
    position: absolute; width: 700px; height: 400px;
    border-radius: 16px; overflow: hidden;
  }
  .card-back { left: 170px; top: 60px; background: var(--navy); }
  .card-front { left: 350px; top: 440px; background: var(--white); }
  .card-front .shape { position: absolute; inset: 0; }

  .brand { display: flex; align-items: center; gap: 12px; }
  .brand-dot { border-radius: 50%; flex: none; }
  .brand-name { font-weight: 600; white-space: nowrap; letter-spacing: 0.5px; }

  .card-back .brand { position: absolute; left: 0; right: 0; top: 0; bottom: 0; justify-content: center; }
  .card-back .brand-dot { width: 26px; height: 26px; background: var(--white); }
  .card-back .brand-name { font-size: 34px; color: var(--white); }

  .card-front .brand { position: absolute; right: 26px; top: 118px; gap: 9px; }
  .card-front .brand-dot { width: 16px; height: 16px; background: var(--navy); }
  .card-front .brand-name { font-size: 20px; color: var(--navy); }

  .holder { position: absolute; left: 66px; top: 120px; color: var(--white); }
  .holder-name { font-size: 21px; font-weight: 700; line-height: 1.2; }
  .holder-title { font-size: 15px; color: var(--text-soft); margin-top: 3px; }
  .holder-rule { width: 64px; height: 2px; background: #7f8fae; margin-top: 14px; }

  .contact { position: absolute; left: 66px; top: 250px; color: var(--text-soft); font-size: 14px; line-height: 1.35; }
  .contact-address { margin-bottom: 8px; }
  .contact-line { display: flex; align-items: center; gap: 9px; }
  .contact-line svg { width: 12px; height: 12px; flex: none; }
</style>
</head>
<body>

<section class="card-set">
  <div class="card card-back">
    <div class="brand"><span class="brand-dot"></span><span class="brand-name">Verdant Pathworks</span></div>
  </div>
  <div class="card card-front">
    <svg class="shape" viewBox="0 0 700 400" aria-hidden="true">
      <path d="M0 0 H436 C506 120 556 280 576 400 H0 Z" fill="var(--grey-soft)"/>
      <path d="M0 0 H422 C492 120 542 280 562 400 H0 Z" fill="var(--grey-band)"/>
      <path d="M0 0 H404 C474 120 524 280 544 400 H0 Z" fill="var(--navy)"/>
    </svg>
    <div class="brand"><span class="brand-dot"></span><span class="brand-name">Verdant Pathworks</span></div>
    <div class="holder">
      <div class="holder-name">Bethany Korvuth</div>
      <div class="holder-title">Customer Relationship Specialist</div>
      <div class="holder-rule"></div>
    </div>
    <div class="contact">
      <div class="contact-address">Alder Crossing<br>Harlow Vale, 2047</div>
      <div class="contact-line"><svg viewBox="0 0 12 12"><path d="M2 1h3l1 3-1.5 1a6 6 0 0 0 2.5 2.5L8 6l3 1v3a1 1 0 0 1-1 1A9 9 0 0 1 1 2a1 1 0 0 1 1-1z" fill="currentColor"/></svg>555-214-7730</div>
      <div class="contact-line"><svg viewBox="0 0 12 12"><rect x="3" y="0.5" width="6" height="11" rx="1" fill="none" stroke="currentColor"/><circle cx="6" cy="9.5" r="0.8" fill="currentColor"/></svg>555-362-4081(office)</div>
      <div class="contact-line"><svg viewBox="0 0 12 12"><rect x="0.5" y="2" width="11" height="8" fill="none" stroke="currentColor"/><path d="M0.5 2 6 6.5 11.5 2" fill="none" stroke="currentColor"/></svg>info@verdantpathworks.com</div>
      <div class="contact-line"><svg viewBox="0 0 12 12"><circle cx="6" cy="6" r="5.5" fill="none" stroke="currentColor"/><path d="M0.5 6h11M6 0.5c-3 3-3 8 0 11M6 0.5c3 3 3 8 0 11" fill="none" stroke="currentColor"/></svg>www.verdantpathworks.com</div>
    </div>
  </div>
</section>

<section class="card-set">
  <div class="card card-back">
    <div class="brand"><span class="brand-dot"></span><span class="brand-name">Verdant Pathworks</span></div>
  </div>
  <div class="card card-front">
    <svg class="shape" viewBox="0 0 700 400" aria-hidden="true">
      <path d="M0 0 H436 C506 120 556 280 576 400 H0 Z" fill="var(--grey-soft)"/>
      <path d="M0 0 H422 C492 120 542 280 562 400 H0 Z" fill="var(--grey-band)"/>
      <path d="M0 0 H404 C474 120 524 280 544 400 H0 Z" fill="var(--navy)"/>
    </svg>
    <div class="brand"><span class="brand-dot"></span><span class="brand-name">Verdant Pathworks</span></div>
    <div class="holder">
      <div class="holder-name">Dominic Ashvale</div>
      <div class="holder-title">Owner</div>
      <div class="holder-rule"></div>
    </div>
    <div class="contact">
      <div class="contact-address">Alder Crossing<br>Harlow Vale, 2047</div>
      <div class="contact-line"><svg viewBox="0 0 12 12"><path d="M2 1h3l1 3-1.5 1a6 6 0 0 0 2.5 2.5L8 6l3 1v3a1 1 0 0 1-1 1A9 9 0 0 1 1 2a1 1 0 0 1 1-1z" fill="currentColor"/></svg>555-214-7730</div>
      <div class="contact-line"><svg viewBox="0 0 12 12"><rect x="3" y="0.5" width="6" height="11" rx="1" fill="none" stroke="currentColor"/><circle cx="6" cy="9.5" r="0.8" fill="currentColor"/></svg>555-362-4081(office)</div>
      <div class="contact-line"><svg viewBox="0 0 12 12"><rect x="0.5" y="2" width="11" height="8" fill="none" stroke="currentColor"/><path d="M0.5 2 6 6.5 11.5 2" fill="none" stroke="currentColor"/></svg>info@verdantpathworks.com</div>
      <div class="contact-line"><svg viewBox="0 0 12 12"><circle cx="6" cy="6" r="5.5" fill="none" stroke="currentColor"/><path d="M0.5 6h11M6 0.5c-3 3-3 8 0 11M6 0.5c3 3 3 8 0 11" fill="none" stroke="currentColor"/></svg>www.verdantpathworks.com</div>
    </div>
  </div>
</section>

<section class="card-set">
  <div class="card card-back">
    <div class="brand"><span class="brand-dot"></span><span class="brand-name">Verdant Pathworks</span></div>
  </div>
  <div class="card card-front">
    <svg class="shape" viewBox="0 0 700 400" aria-hidden="true">
      <path d="M0 0 H436 C506 120 556 280 576 400 H0 Z" fill="var(--grey-soft)"/>
      <path d="M0 0 H422 C492 120 542 280 562 400 H0 Z" fill="var(--grey-band)"/>
      <path d="M0 0 H404 C474 120 524 280 544 400 H0 Z" fill="var(--navy)"/>
    </svg>
    <div class="brand"><span class="brand-dot"></span><span class="brand-name">Verdant Pathworks</span></div>
    <div class="holder">
      <div class="holder-name">Luca Brennwick</div>
      <div class="holder-title">Vice President of Sales</div>
      <div class="holder-rule"></div>
    </div>
    <div class="contact">
      <div class="contact-address">Alder Crossing<br>Harlow Vale, 2047</div>
      <div class="contact-line"><svg viewBox="0 0 12 12"><path d="M2 1h3l1 3-1.5 1a6 6 0 0 0 2.5 2.5L8 6l3 1v3a1 1 0 0 1-1 1A9 9 0 0 1 1 2a1 1 0 0 1 1-1z" fill="currentColor"/></svg>555-214-7730</div>
      <div class="contact-line"><svg viewBox="0 0 12 12"><rect x="3" y="0.5" width="6" height="11" rx="1" fill="none" stroke="currentColor"/><circle cx="6" cy="9.5" r="0.8" fill="currentColor"/></svg>555-362-4081(office)</div>
      <div class="contact-line"><svg viewBox="0 0 12 12"><rect x="0.5" y="2" width="11" height="8" fill="none" stroke="currentColor"/><path d="M0.5 2 6 6.5 11.5 2" fill="none" stroke="currentColor"/></svg>info@verdantpathworks.com</div>
      <div class="contact-line"><svg viewBox="0 0 12 12"><circle cx="6" cy="6" r="5.5" fill="none" stroke="currentColor"/><path d="M0.5 6h11M6 0.5c-3 3-3 8 0 11M6 0.5c3 3 3 8 0 11" fill="none" stroke="currentColor"/></svg>www.verdantpathworks.com</div>
    </div>
  </div>
</section>

</body>
</html>
```